Bref créative
Veloran Lending Group
Mortgage Lender
Professional
Gustav Kolbe
President
318 Birchwell Avenue
Regina, SK, S2K 8P4
Ph (306) 555-0142
Cl (306) 555-0187
Fx (306) 555-0143
gustav@veloran.ca
www.veloran.ca

```html
<!DOCTYPE html>
<html lang="en">
<head>
<meta charset="utf-8">
<title>Veloran Lending Group — Business Cards</title>
<link rel="stylesheet" href="https://fonts.googleapis.com/css2?family=Cinzel:wght@400;600&family=Cormorant+SC:wght@500;600&display=swap">
<style>
  :root {
    --backdrop: #3b3b3b;
    --card-white: #ffffff;
    --card-black: #0c0c0c;
    --brand-red: #e0201b;
    --ink: #1a1a1a;
    --rule: #9a9a9a;
    --text-light: #f2f2f2;
  }
  * { margin: 0; padding: 0; box-sizing: border-box; }
  html, body { width: 1200px; height: 901px; overflow: hidden; }
  body { background: var(--backdrop); position: relative; }

  .card {
    position: absolute;
    width: 540px;
    height: 309px;
    overflow: hidden;
    box-shadow: 0 10px 30px rgba(0,0,0,.45);
  }
  .card--front { left: 70px; top: 130px; background: var(--card-black); }
  .card--back  { left: 590px; top: 460px; background: var(--card-white); }

  /* Wordmark */
  .wordmark { text-align: center; font-family: "Cinzel", serif; color: var(--ink); font-weight: 400; }
  .wordmark__main {
    display: flex; align-items: center; justify-content: center; gap: 10px;
    font-size: 28px; letter-spacing: 1px; line-height: 1;
  }
  .wordmark__square { width: 16px; height: 16px; background: var(--brand-red); }
  .wordmark__sub {
    display: flex; align-items: center; justify-content: center; gap: 10px;
    margin-top: 6px; font-size: 12px; letter-spacing: 6px;
  }
  .wordmark__sub::before, .wordmark__sub::after {
    content: ""; width: 70px; height: 1px; background: var(--rule);
  }

  /* Front card */
  .front__brand-panel {
    position: absolute; left: 0; top: 0; width: 380px; height: 150px;
    background: var(--card-white);
    display: flex; flex-direction: column; align-items: center; justify-content: center;
  }
  .front__brand-panel .wordmark__main { font-size: 24px; }
  .front__rule { position: absolute; left: 40px; top: 128px; width: 300px; height: 1px; background: var(--rule); }

  .front__mark {
    position: absolute; left: 420px; top: 110px; width: 70px; height: 70px;
    background: var(--brand-red);
  }
  .front__web {
    position: absolute; left: 400px; top: 200px; width: 110px; text-align: center;
    font-family: "Cormorant SC", serif; font-weight: 500; font-size: 12px;
    letter-spacing: .5px; color: var(--text-light);
  }

  .contact {
    position: absolute; left: 34px; top: 176px;
    font-family: "Cormorant SC", serif; font-weight: 500;
    color: var(--text-light); font-size: 12px; line-height: 13px; letter-spacing: .4px;
  }
  .contact__name { color: var(--brand-red); font-size: 15px; line-height: 18px; margin-bottom: 4px; }
  .contact__title { color: var(--text-light); font-size: 12px; }
  .contact__divider { color: var(--brand-red); margin: 0 4px; }
  .contact__address { margin-bottom: 4px; }
  .contact__label { color: var(--brand-red); margin-right: 4px; }

  /* Back card */
  .card--back .wordmark {
    position: absolute; left: 0; right: 0; top: 50%; transform: translateY(-50%);
  }
</style>
</head>
<body>

  <section class="card card--front" aria-label="Business card front">
    <div class="front__brand-panel">
      <div class="wordmark">
        <div class="wordmark__main">VELORAN <span class="wordmark__square"></span> LENDING</div>
        <div class="wordmark__sub">GROUP</div>
      </div>
    </div>
    <div class="front__rule"></div>

    <div class="front__mark"></div>
    <div class="front__web">www.veloran.ca</div>

    <div class="contact">
      <div class="contact__name">Gustav Kolbe<span class="contact__divider">|</span><span class="contact__title">President</span></div>
      <div class="contact__address">318 Birchwell Avenue<br>Regina, SK, S2K 8P4</div>
      <div><span class="contact__label">P:</span>(306) 555-0142</div>
      <div><span class="contact__label">C:</span>(306) 555-0187</div>
      <div><span class="contact__label">F:</span>(306) 555-0143</div>
      <div><span class="contact__label">E:</span>gustav@veloran.ca</div>
    </div>
  </section>

  <section class="card card--back" aria-label="Business card back">
    <div class="wordmark">
      <div class="wordmark__main">VELORAN <span class="wordmark__square"></span> LENDING</div>
      <div class="wordmark__sub">GROUP</div>
    </div>
  </section>

</body>
</html>
```